Flyer-Design für Musikverein - Jugendkapelle
Zielgruppe
Musikverein Tannbrück
Unsere Zielgruppe sind Kinder und Jugendliche, die ein Instrument erlernen wollen.
Der Einstieg der jüngsten geht in einem Alter ab ca. 8 Jahren los. Die meisten neuen Musiker steigen zwischen 10 - 14 Jahren ein.
Der Flyer soll aber auch geeignet sein um an Grund- und weiterführenden Schulen ausgelegt werden zu können um Musiker für die Jugendkapelle zu gewinnen. Dementsprechend frisch und interessant soll der Flyer gestaltet sein.
Aufgabenstellung
Es soll ansprechend sein für Jugendliche, frisch, fröhlich und soll das Interesse der jugendlichen mit dem Design wecken.
Es soll die Jugendlichkeit, die Blasmusik und das Vereinsleben miteinander verbinden, sowie die Vorteile und der Spaß an der Musik (Instrument erlernen, Spaß am Musizieren, neue Freunde und Kameradschaft und auch Freizeitaktivitäten) miteinander darstellen.

```html
<!DOCTYPE html>
<html lang="de">
<head>
<meta charset="utf-8">
<title>Flyer Jugendkapelle – Musikverein Tannbrück</title>
<link rel="stylesheet" href="https://fonts.googleapis.com/css2?family=Quicksand:wght@500;700&family=Lato:ital,wght@0,300;0,400;0,700;1,700&display=swap">
<style>
  :root {
    --teal: #007b79;
    --orange: #f57b0c;
    --white: #ffffff;
    --stage: #e8e5e1;
    --footer-text: #cfe3e2;
  }
  html, body {
    margin: 0;
    padding: 0;
    width: 1200px;
    height: 798px;
    overflow: hidden;
    background: var(--stage);
  }
  .canvas {
    position: relative;
    width: 1200px;
    height: 798px;
  }
  .flyer {
    position: absolute;
    width: 540px;
    height: 540px;
    overflow: hidden;
    background: var(--white);
    box-shadow: 0 2px 10px rgba(0,0,0,0.12);
  }
  .flyer svg {
    display: block;
    width: 540px;
    height: 540px;
  }
  .flyer--front { left: 60px; top: 200px; }
  .flyer--back  { left: 630px; top: 70px; }

  .headline,
  .subline {
    font-family: "Quicksand", sans-serif;
    font-weight: 700;
  }

  .back-copy {
    position: absolute;
    left: 18px;
    top: 265px;
    font-family: "Lato", sans-serif;
    font-size: 10.8px;
    line-height: 13.8px;
    color: var(--white);
    white-space: nowrap;
  }
  .back-copy p { margin: 0; }
  .back-copy .offer { font-weight: 700; word-spacing: 0.5px; }
  .back-copy .intro { margin-top: 13.8px; font-weight: 400; }
  .back-copy .band { margin-top: 13.8px; font-weight: 400; }
  .back-copy .invite {
    font-weight: 700;
    font-style: italic;
    line-height: 15px;
  }
  .back-copy strong { font-weight: 700; }
  .back-copy .signoff {
    margin-top: 10px;
    font-weight: 300;
    color: var(--footer-text);
  }
</style>
</head>
<body>
<div class="canvas">

  <!-- Vorderseite -->
  <section class="flyer flyer--front">
    <svg viewBox="0 0 950 950" xmlns="http://www.w3.org/2000/svg">
      <defs>
        <linearGradient id="instrumentTones" x1="0" y1="0" x2="1" y2="1">
          <stop offset="0" stop-color="#f4a23a"/>
          <stop offset="0.4" stop-color="#e8653a"/>
          <stop offset="0.7" stop-color="#c9487a"/>
          <stop offset="1" stop-color="#2aa388"/>
        </linearGradient>
      </defs>
      <rect width="950" height="950" fill="var(--white)"/>
      <polygon class="instrument-collage" role="img"
               aria-label="Bunte Illustration mit Musikinstrumenten, Kopfhörern, Mikrofonen und Notenschlüsseln"
               points="0,0 950,0 950,170 0,690" fill="url(#instrumentTones)" opacity="0.85"/>
      <polygon points="0,688 950,165 950,950 0,950" fill="var(--teal)"/>
      <polygon points="0,725 950,208 950,214 0,731" fill="var(--orange)"/>
      <polygon points="0,731 950,214 950,336 0,853" fill="var(--white)"/>
      <polygon points="0,853 950,336 950,342 0,859" fill="var(--orange)"/>
      <polygon points="0,945 950,452 950,460 0,953" fill="var(--white)"/>

      <text class="headline" x="0" y="0" font-size="68" fill="var(--orange)"
            textLength="850" lengthAdjust="spacingAndGlyphs"
            transform="translate(104,756) rotate(-29.2)">MUSIK MACHT FREU(N)DE.</text>
      <text class="subline" x="0" y="0" font-size="42" fill="var(--white)"
            textLength="546" lengthAdjust="spacingAndGlyphs"
            transform="translate(258,782) rotate(-29.2)">Wer will Musiker werden?</text>
    </svg>
  </section>

  <!-- Rückseite -->
  <section class="flyer flyer--back">
    <svg viewBox="0 0 942 942" xmlns="http://www.w3.org/2000/svg">
      <rect width="942" height="942" fill="var(--white)"/>
      <line x1="0" y1="128" x2="792" y2="564" stroke="var(--orange)" stroke-width="6"/>
      <line x1="0" y1="140" x2="790" y2="576" stroke="var(--teal)" stroke-width="12"/>
      <polygon points="0,252 942,770 942,942 0,942" fill="var(--teal)"/>
      <polygon points="705,615 942,482 942,752" fill="var(--orange)"/>
      <line x1="0" y1="236" x2="942" y2="754" stroke="var(--orange)" stroke-width="6"/>
      <line x1="0" y1="246" x2="942" y2="764" stroke="var(--white)" stroke-width="6"/>

      <text class="headline" x="0" y="0" font-size="44" fill="var(--orange)"
            textLength="660" lengthAdjust="spacingAndGlyphs"
            transform="translate(38,218) rotate(28.7)">Hast du Lust bei uns mitzumachen?</text>
    </svg>

    <div class="back-copy">
      <p class="offer">Wir bieten im Bereich Blasmusik<br>qualifizierten Musikunterricht für Kinder<br>und Jugendliche an. Unsere Leistungen sind<br>Einzelunterricht, Lehrkräfte mit Musikausbildung<br>und langjähriger pädagogischer Erfahrung.</p>
      <p class="intro">Der Musikverein Tannbrück e.V. bietet allen musikinteressierten Kin-<br>dern, Jugendlichen und Erwachsenen die Möglichkeit ein Instrument<br>zu erlernen. Bei uns kannst du <strong>Trompete/Flügelhorn, Tuba, Tenorhorn/Bari-<br>ton/Posaune, Waldhorn, Klarinette, Saxophon, Querflöte und Schlagzeug</strong> lernen.</p>
      <p class="band">In unserer Jugendkapelle haben die Kinder und Jugendlichen die Möglichkeit nach 1-2 jähri-<br>ger Ausbildung in der Gruppe zu spielen und zu üben. Danach geht es an das Musizieren im<br>großen Orchester. Letztendlich entscheiden die Dirigenten und Ausbilder über den Eintritt in<br>die jeweiligen Orchester.</p>
      <p class="invite">Oder du kannst schon ein Instrument spielen und willst mit anderen gemeinsam musizieren? Dann<br>komm doch in die Jugendkapelle „TAKTWERK“.</p>
      <p class="signoff">Musikverein Tannbrück - www.tannbrueck-musikverein.de</p>
    </div>
  </section>

</div>
</body>
</html>
```